WIX Landing Page for Cosmetic Distributor

We want to relaunch our current website (dravolin.ch), and are looking for a template from you on WIX. We are a distributor of chemical raw materials for beauty products. Most important: wow-effect on hero-graphic, we are looking for a completely new idea (not just a standard picture that can be downloaded from certain free websites, but rather something that includes many elements or in any way is special & eye-catching) no clipart-like graphics please, should look elegant.
• Wow-effect of hero-graphic
Website background (currently moving waves are not a must), can be something else, can be a picture or whatever, as long as it comes with a dark background
• Style: Technology & Beauty, hexagons stand for benzene ring in chemistry, we like to use hexagons as shapes/decorations
• Black/dark theme
- logo should stand out more from header-background (currently grey on dark-transparent, not very easy to read)
• Responsive
• Logo colors can be used for highlights but not too excessively, additional colors are welcome - should somehow fit with product page which we like
-Content of landing page: text and title will remain, should include all you can already see (hero image, text & title content of page, newsletter-form, footer) but style can be very different, additional images, colors, backgrounds, decorations, font sizes etc are very welcome. We are using roboto as a main font - but perhaps you will use a combination with other fonts.
• Please change the 6 tiles (logistik etc), not happy & too overloaded. Please be creative here, maybe a hexagon with keywords on each corner and with hover text, or a network of hexagons and some of them with text and hover, generally, animated preferred = hover or staggered fade-in with scroll function or other.
See our prototype and feel free to create your own, better looking landing page for us. We would like you to create a template in WIX that we can use. You can copy our prototype to have a point to start with.
Prototype: https://studio318907.wixsite.com/dravolin
Target Market(s)
Cosmetic Industry Switzerland, Austria, Germany
Industry/Entity Type
cosmetic raw matierials industry (technical, beauty)
Number of Pages Required
1 page
Font styles to use
Other font styles liked:
- Roboto
Requirements
Must have
- hero-image, eye-catching

```html
<!DOCTYPE html>
<html lang="de">
<head>
<meta charset="utf-8">
<title>Dravolin – creative chemicals</title>
<link href="https://fonts.googleapis.com/css2?family=Inter:wght@300;400;500;600&display=swap" rel="stylesheet">
<style>
:root{
  --black:#030305;
  --white:#ffffff;
  --soft:#d9d9dc;
  --orange:#ff6a00;
  --orange-deep:#e85a00;
  --grey-frame:#5a5a5e;
  --font:"Inter", "Helvetica Neue", Arial, sans-serif;
}
*{margin:0;padding:0;box-sizing:border-box}
html,body{width:1200px;height:3524px;overflow:hidden;background:var(--black)}
body{position:relative;font-family:var(--font);color:var(--white)}
.abs{position:absolute}
section,footer{position:absolute;left:0;width:1200px;overflow:hidden}

.dark-wave{
  background:
    radial-gradient(ellipse 520px 220px at 15% 20%, rgba(60,66,82,.55), transparent 70%),
    radial-gradient(ellipse 600px 260px at 85% 70%, rgba(52,58,74,.5), transparent 70%),
    radial-gradient(ellipse 400px 180px at 50% 100%, rgba(40,44,56,.5), transparent 70%),
    var(--black);
}
.glow{position:absolute;border-radius:50%;background:radial-gradient(circle, rgba(255,214,140,.85), rgba(255,190,90,.25) 55%, transparent 72%)}

/* header */
.brand{left:82px;top:30px;display:flex;align-items:center;gap:10px}
.brand-mark{width:34px;height:34px;border-radius:50%;background:var(--orange)}
.brand-name{font-size:30px;font-weight:500;line-height:1}
.brand-sub{font-size:12px;font-weight:400;margin-top:3px}
.nav{right:96px;top:56px;display:flex;gap:26px;font-size:12.5px;color:var(--soft)}

/* pager dots */
.pager{display:flex;flex-direction:column;gap:11px}
.pager span{width:9px;height:9px;border-radius:50%;background:var(--white)}
.pager span.on{background:var(--orange)}

/* hero */
.hero{top:0;height:568px}
.hero-title{left:80px;top:226px;font-size:38px;font-weight:300;line-height:1.35}
.hero-title strong{font-weight:600;display:block}
.hero-lead{left:80px;top:350px;font-size:19px;font-weight:300;line-height:1.4;width:440px}
.hero-visual{left:620px;top:92px}

/* partner */
.partner{top:568px;height:413px}
.partner-title{left:0;width:1200px;top:722px;text-align:center;font-size:57px;font-weight:300;line-height:1.28;letter-spacing:.5px}

/* features */
.features{top:981px;height:517px;
  background:
    radial-gradient(ellipse 620px 460px at 100% 100%, var(--orange) 0%, rgba(232,90,0,.8) 30%, transparent 75%),
    linear-gradient(135deg,#16171b,#0d0e11 50%,#121316);
}
.features-title{left:543px;top:1110px;font-size:38px;font-weight:300}
.check{display:flex;gap:8px;font-size:15px;font-weight:300;line-height:1.3;width:215px}
.check svg{flex:none;margin-top:3px}

/* tiles: honeycomb */
.tiles{top:1498px;height:862px}
.tile{position:absolute;width:232px;height:268px}
.tile svg.frame{position:absolute;inset:0}
.tile-body{position:absolute;left:30px;right:30px;top:64px;text-align:center}
.tile-body svg{display:block;margin:0 auto 12px}
.tile-name{font-size:18px;font-weight:500;line-height:1.3;margin-bottom:8px}
.tile-text{font-size:11.5px;font-weight:300;line-height:1.45;color:var(--soft)}
.tile.accent .tile-text{color:var(--white)}

/* success */
.success{top:2360px;height:483px}
.success-title{left:205px;top:2466px;font-size:55px;font-weight:300;line-height:1.32}
.success-text{left:212px;top:2634px;font-size:20px;font-weight:300;line-height:1.35;color:var(--soft)}

/* newsletter */
.newsletter{top:2843px;height:420px;
  background:
    radial-gradient(ellipse 700px 260px at 0% 100%, var(--orange) 0%, rgba(232,90,0,.7) 35%, transparent 75%),
    linear-gradient(160deg,#17181c,#0c0d10 60%,#121316);
}
.nl-title{left:0;width:1158px;top:2932px;text-align:center;font-size:38px;font-weight:300}
.nl-col{top:3010px;font-size:20px;font-weight:300;line-height:1.35}
.nl-rule{width:1px;height:80px;background:var(--soft);top:3005px}
.nl-form{left:343px;top:3118px;width:512px;height:59px;display:flex;border:1px solid var(--soft)}
.nl-input{flex:1;display:flex;align-items:center;padding-left:38px;font-size:14px;color:var(--soft)}
.nl-send{width:152px;background:var(--white);color:var(--black);display:flex;align-items:center;justify-content:center;font-size:14px;font-weight:500}

/* footer */
.site-footer{top:3263px;height:261px}
.foot-contact{left:157px;top:3308px;font-size:14px;line-height:1.4}
.foot-links{left:513px;top:3312px;font-size:14px;line-height:28px}
.foot-social{left:858px;top:3323px;display:flex;gap:14px}
.foot-social span{width:20px;height:20px;border-radius:50%;background:var(--white)}
.foot-legal{left:856px;top:3362px;font-size:14px}
.foot-copy{font-size:14px;top:3435px}
</style>
</head>
<body>

<!-- Hero -->
<section class="hero dark-wave">
  <div class="glow" style="left:120px;top:480px;width:34px;height:34px"></div>
  <div class="glow" style="left:435px;top:105px;width:24px;height:24px"></div>
  <div class="glow" style="left:1150px;top:130px;width:30px;height:30px"></div>
  <div class="glow" style="left:465px;top:430px;width:26px;height:26px"></div>
  <div class="glow" style="left:570px;top:180px;width:16px;height:16px"></div>
</section>
<svg class="abs hero-visual" width="500" height="476" viewBox="0 0 500 476">
  <defs>
    <radialGradient id="heroPhoto" cx="52%" cy="42%" r="60%">
      <stop offset="0" stop-color="#d8b09c"/>
      <stop offset=".45" stop-color="#8a6252"/>
      <stop offset=".8" stop-color="#2a1f1c"/>
      <stop offset="1" stop-color="#0c0b0c"/>
    </radialGradient>
    <linearGradient id="heroRing" x1="0" y1="0" x2="1" y2="1">
      <stop offset="0" stop-color="#ff6a00"/>
      <stop offset="1" stop-color="#ff6a00" stop-opacity="0"/>
    </linearGradient>
  </defs>
  <polygon points="250,6 461,128 461,372 250,494 39,372 39,128" fill="none" stroke="#3a3d46" stroke-width="1"/>
  <polygon points="250,28 442,139 442,361 250,472 58,361 58,139" fill="none" stroke="url(#heroRing)" stroke-width="2.5"/>
  <polygon points="250,52 421,151 421,349 250,448 79,349 79,151" fill="url(#heroPhoto)" role="img" aria-label="Porträtfoto einer Frau mit dunklem, zurückgekämmtem Haar"/>
  <polygon points="460,40 478,50 478,71 460,81 442,71 442,50" fill="none" stroke="#ff6a00" stroke-width="1.5"/>
  <polygon points="30,70 44,78 44,94 30,102 16,94 16,78" fill="none" stroke="#5a5a5e" stroke-width="1.5"/>
  <polygon points="18,300 30,307 30,321 18,328 6,321 6,307" fill="#ff6a00"/>
  <line x1="442" y1="139" x2="460" y2="81" stroke="#ff6a00" stroke-width="1" stroke-opacity=".6"/>
  <line x1="58" y1="139" x2="30" y2="102" stroke="#5a5a5e" stroke-width="1"/>
</svg>
<div class="abs brand">
  <span class="brand-mark"></span>
  <div><div class="brand-name">Dravolin</div><div class="brand-sub">creative chemicals</div></div>
</div>
<nav class="abs nav"><span>Home</span><span>Producte</span><span>News</span><span>Partner</span><span>Uber uns</span><span>Kontakt</span><span>Datenschutz</span></nav>
<h1 class="abs hero-title">We sell creative chemicals.<strong>We care about your success</strong></h1>
<p class="abs hero-lead">Creative Raw Materials for Personal Care and Home Care Industry</p>
<div class="abs pager" style="left:1107px;top:266px"><span class="on"></span><span></span><span></span><span></span><span></span><span></span></div>

<!-- Partner -->
<section class="partner dark-wave">
  <div class="glow" style="left:55px;top:165px;width:28px;height:28px"></div>
  <div class="glow" style="left:465px;top:355px;width:26px;height:26px"></div>
  <div class="glow" style="left:1150px;top:60px;width:28px;height:28px"></div>
</section>
<h2 class="abs partner-title">Creative Chemicals<br>Dravolin Ihr Partner</h2>
<div class="abs pager" style="left:1107px;top:745px"><span></span><span class="on"></span><span></span><span></span><span></span><span></span></div>

<!-- Features -->
<section class="features"></section>
<svg class="abs" style="left:130px;top:1064px" width="340" height="384" viewBox="0 0 340 384">
  <defs><radialGradient id="featPhoto" cx="48%" cy="50%" r="60%"><stop offset="0" stop-color="#d2a894"/><stop offset=".5" stop-color="#6a4a3e"/><stop offset="1" stop-color="#1d1d20"/></radialGradient></defs>
  <polygon points="170,2 338,98 338,286 170,382 2,286 2,98" fill="url(#featPhoto)" role="img" aria-label="Foto einer Frau, die Creme auf die Wange aufträgt"/>
  <polygon points="170,2 338,98 338,286 170,382 2,286 2,98" fill="none" stroke="var(--grey-frame)" stroke-width="4"/>
</svg>
<h2 class="abs features-title">Dies ist ein Titel</h2>
<div class="abs check" style="left:543px;top:1186px"><svg width="13" height="13" viewBox="0 0 13 13"><circle cx="6.5" cy="6.5" r="5.5" fill="none" stroke="#fff"/><path d="M4 6.7l1.8 1.8L9.2 5" fill="none" stroke="#fff"/></svg><span>Breite Auswahl an erstklassigen Rohstoffen</span></div>
<div class="abs check" style="left:800px;top:1186px;width:245px"><svg width="13" height="13" viewBox="0 0 13 13"><circle cx="6.5" cy="6.5" r="5.5" fill="none" stroke="#fff"/><path d="M4 6.7l1.8 1.8L9.2 5" fill="none" stroke="#fff"/></svg><span>Personal Care, Home Care und technische Industrie</span></div>
<div class="abs check" style="left:543px;top:1279px"><svg width="13" height="13" viewBox="0 0 13 13"><circle cx="6.5" cy="6.5" r="5.5" fill="none" stroke="#fff"/><path d="M4 6.7l1.8 1.8L9.2 5" fill="none" stroke="#fff"/></svg><span>Anspruchsvolle Märkte Schweiz, Österreich und Deutschland</span></div>
<div class="abs check" style="left:806px;top:1279px;width:225px"><svg width="13" height="13" viewBox="0 0 13 13"><circle cx="6.5" cy="6.5" r="5.5" fill="none" stroke="#fff"/><path d="M4 6.7l1.8 1.8L9.2 5" fill="none" stroke="#fff"/></svg><span>Exklusive Distribution namhafter Lieferpartner wie Norvek, Altispec, Cerapharm, Luvenza...</span></div>
<div class="abs pager" style="left:1117px;top:1177px"><span></span><span></span><span class="on"></span><span></span><span></span><span></span></div>

<!-- Tiles -->
<section class="tiles dark-wave">
  <div class="glow" style="left:172px;top:66px;width:28px;height:28px"></div>
  <div class="glow" style="left:955px;top:90px;width:36px;height:36px"></div>
  <div class="glow" style="left:1128px;top:236px;width:32px;height:32px"></div>
  <div class="glow" style="left:120px;top:374px;width:28px;height:28px"></div>
  <div class="glow" style="left:1040px;top:520px;width:40px;height:40px"></div>
  <div class="glow" style="left:390px;top:780px;width:26px;height:26px"></div>
</section>
<svg width="0" height="0" class="abs"><defs>
  <linearGradient id="tileStroke" x1="0" y1="0" x2="0" y2="1"><stop offset="0" stop-color="#ff6a00"/><stop offset="1" stop-color="#7d6a5c"/></linearGradient>
  <linearGradient id="tileFill" x1="0" y1="0" x2="1" y2="1"><stop offset="0" stop-color="#ff7a1a"/><stop offset="1" stop-color="#b84500"/></linearGradient>
</defs></svg>

<div class="tile" style="left:176px;top:1640px">
  <svg class="frame" width="232" height="268" viewBox="0 0 232 268"><polygon points="116,2 230,68 230,200 116,266 2,200 2,68" fill="#07070a" stroke="url(#tileStroke)" stroke-width="3"/></svg>
  <div class="tile-body"><svg width="40" height="36" viewBox="0 0 44 40" fill="none" stroke="#ff6a00" stroke-width="2"><circle cx="22" cy="8" r="5"/><path d="M14 22a8 8 0 0116 0"/><path d="M3 10v14l10 10h7M41 10v14L31 34h-7"/></svg>
  <div class="tile-name">Projekt Begleitung</div><div class="tile-text">Massgeschneiderte Lösungen, Studien, schnelle Bemusterung.</div></div>
</div>
<div class="tile accent" style="left:416px;top:1640px">
  <svg class="frame" width="232" height="268" viewBox="0 0 232 268"><polygon points="116,2 230,68 230,200 116,266 2,200 2,68" fill="url(#tileFill)"/></svg>
  <div class="tile-body"><svg width="44" height="34" viewBox="0 0 48 36" fill="none" stroke="#fff" stroke-width="2"><rect x="3" y="6" width="26" height="20"/><path d="M29 12h9l6 8v6H29"/><circle cx="11" cy="29" r="3.5"/><circle cx="37" cy="29" r="3.5"/></svg>
  <div class="tile-name">Logistik</div><div class="tile-text">Eigenes Rohstofflager, rascher Lieferservice.</div></div>
</div>
<div class="tile" style="left:656px;top:1640px">
  <svg class="frame" width="232" height="268" viewBox="0 0 232 268"><polygon points="116,2 230,68 230,200 116,266 2,200 2,68" fill="#07070a" stroke="url(#tileStroke)" stroke-width="3"/></svg>
  <div class="tile-body"><svg width="42" height="32" viewBox="0 0 44 34" fill="none" stroke="#ff6a00" stroke-width="2"><path d="M4 11h34M30 4l8 7-8 7M40 23H6M14 16l-8 7 8 7"/></svg>
  <div class="tile-name">Know-How Transfer</div><div class="tile-text">Neue Ideen und Trends für innovative Projekte.</div></div>
</div>
<div class="tile" style="left:296px;top:1841px">
  <svg class="frame" width="232" height="268" viewBox="0 0 232 268"><polygon points="116,2 230,68 230,200 116,266 2,200 2,68" fill="#07070a" stroke="url(#tileStroke)" stroke-width="3"/></svg>
  <div class="tile-body"><svg width="38" height="38" viewBox="0 0 44 44" fill="none" stroke="#ff6a00" stroke-width="2"><circle cx="22" cy="15" r="9"/><path d="M6 42c0-9 7-15 16-15s16 6 16 15z"/></svg>
  <div class="tile-name">Kundenorientierung</div><div class="tile-text">Erste Anlaufstelle mit der besten Lösung.</div></div>
</div>
<div class="tile" style="left:536px;top:1841px">
  <svg class="frame" width="232" height="268" viewBox="0 0 232 268"><polygon points="116,2 230,68 230,200 116,266 2,200 2,68" fill="#07070a" stroke="url(#tileStroke)" stroke-width="3"/></svg>
  <div class="tile-body"><svg width="28" height="40" viewBox="0 0 32 44" fill="none" stroke="#ff6a00" stroke-width="2"><rect x="4" y="2" width="24" height="40" rx="3"/><path d="M13 37h6"/></svg>
  <div class="tile-name">Erreichbarkeit</div><div class="tile-text">Ein Team in greifbarer Nähe, schnell verfügbar.</div></div>
</div>
<div class="tile accent" style="left:776px;top:1841px">
  <svg class="frame" width="232" height="268" viewBox="0 0 232 268"><polygon points="116,2 230,68 230,200 116,266 2,200 2,68" fill="url(#tileFill)"/></svg>
  <div class="tile-body"><svg width="38" height="38" viewBox="0 0 40 40" fill="none" stroke="#fff" stroke-width="2"><circle cx="27" cy="13" r="5"/><path d="M27 2v4M27 20v4M16 13h4M34 13h4M4 36l16-16M10 36l10-10M4 30l10-10"/></svg>
  <div class="tile-name">Kompetenz</div><div class="tile-text">Langjährige Erfahrung, umfassende Beratung.</div></div>
</div>
<div class="abs pager" style="left:1126px;top:1865px"><span></span><span></span><span></span><span class="on"></span><span></span><span></span></div>

<!-- Success -->
<section class="success dark-wave">
  <div class="glow" style="left:115px;top:0;width:26px;height:26px"></div>
  <div class="glow" style="left:125px;top:408px;width:34px;height:34px"></div>
  <div class="glow" style="left:1140px;top:50px;width:28px;height:28px"></div>
</section>
<h2 class="abs success-title">We Care About<br>Your Success</h2>
<p class="abs success-text">Ihr Erfolg liegt uns am Herzen.<br>Ihr Erfolg spornt uns an.<br>Wir bringen sie weiter.</p>
<svg class="abs" style="left:673px;top:2405px" width="340" height="384" viewBox="0 0 340 384">
  <defs><radialGradient id="succPhoto" cx="55%" cy="48%" r="60%"><stop offset="0" stop-color="#d6ad96"/><stop offset=".5" stop-color="#7a5c48"/><stop offset="1" stop-color="#1b1714"/></radialGradient></defs>
  <polygon points="170,2 338,60 338,320 170,382 2,320 2,60" fill="url(#succPhoto)" role="img" aria-label="Porträtfoto einer Frau mit langem blondem geflochtenem Haar"/>
  <polygon points="170,2 338,60 338,320 170,382 2,320 2,60" fill="none" stroke="var(--grey-frame)" stroke-width="4"/>
</svg>
<div class="abs pager" style="left:1135px;top:2550px"><span></span><span></span><span></span><span></span><span class="on"></span><span></span></div>

<!-- Newsletter -->
<section class="newsletter"></section>
<h2 class="abs nl-title">Newsletter-Anmeldung</h2>
<p class="abs nl-col" style="left:166px">Erhalten Sie zeitnah<br>Informationen über<br>Produktneuheiten</p>
<div class="abs nl-rule" style="left:409px"></div>
<p class="abs nl-col" style="left:460px">Verfolgen Sie wertvolle<br>regulatorische Hinweise</p>
<div class="abs nl-rule" style="left:716px"></div>
<p class="abs nl-col" style="left:747px;top:3014px">Lassen Sie sich von unseren<br>Ideen inspirieren</p>
<div class="abs nl-form"><div class="nl-input">Type your email</div><div class="nl-send">SEND</div></div>
<div class="abs pager" style="left:1131px;top:2993px"><span></span><span></span><span></span><span></span><span></span><span class="on"></span></div>

<!-- Footer -->
<footer class="site-footer dark-wave">
  <div class="glow" style="left:55px;top:88px;width:22px;height:22px"></div>
  <div class="glow" style="left:48px;top:156px;width:22px;height:22px"></div>
</footer>
<p class="abs foot-contact">Wir stehen Ihnen zur Verfügung:<br>044 555 01 80<br>Mo - Fr 8-17 Uhr<br>Kontakt</p>
<p class="abs foot-copy" style="left:157px">2022 Dravolin AG</p>
<p class="abs foot-links">Über uns<br>Kontakt<br>Partner<br>Produkte</p>
<div class="abs foot-social" aria-label="Soziale Netzwerke"><span></span><span></span><span></span></div>
<p class="abs foot-legal">Datenschutz | Impressum</p>
<p class="abs foot-copy" style="left:856px">©2022 von Dravolin.</p>

</body>
</html>
```